Powerpoint for consulting dentalpractices on management, improvement, and benchmarks

Fase 1: create 8-15 slides to be used for the model. The are the basic slideexamples for future presentation.
colour scheme and font types as in attachment for older powerpoint. Fonts, logo and colourscheme stay the same. Newer slidedeck contains newer ideas for new presentations. Smaller logo maybe better to be used for all slides. Normal logo for starting and end slide. Open for your inspiration and new suggestions
Fase 2 create slidemaster to enable us to create new slidedesks faster.

Target Market(s)

Dentalpractices (no dental images in powerpoint)

Industry/Entity Type

Dental practices

Font styles to use
Other font styles liked:
• Roobert for heading Normal Text Inter

Requirements
Must have
• Different slidemaster basic slides to quickly create slides with full slide pictures which still have a Molvera touch. Content slides, slides with bullets and slides to show 3 -5 subjects
Nice to have
• New styling element for recognition of brand
Should not have
• round edges, complex slide master

```html
<!DOCTYPE html>
<html lang="en">
<head>
<meta charset="utf-8">
<title>Molvera – Slide Templates</title>
<link href="https://fonts.googleapis.com/css2?family=Montserrat:wght@300;400;500;600&display=swap" rel="stylesheet">
<style>
  :root{
    --stage:#c9c9cb;
    --blue:#0d57a7;
    --blue-deep:#0a4a8f;
    --green:#6cbf43;
    --grey:#d9dadb;
    --grey-light:#e8e9ea;
    --ink:#333a40;
    --white:#ffffff;
  }
  html,body{margin:0;padding:0;}
  body{
    width:1200px;height:1104px;overflow:hidden;position:relative;
    background:var(--stage);
    font-family:"Montserrat",Arial,sans-serif;
  }
  .defs{position:absolute;width:0;height:0;}
  .slide{
    position:absolute;width:245.6px;height:138px;
    background:var(--white);
    box-shadow:0 2px 4px rgba(0,0,0,.28);
    font-family:"Montserrat",Arial,sans-serif;
  }
  .slide text{font-family:"Montserrat",Arial,sans-serif;}
  .title{font-size:9px;font-weight:400;letter-spacing:.2px;}
  .label{font-size:3.6px;font-weight:400;}
  .small{font-size:3px;font-weight:400;}
  .caps{font-size:3.6px;font-weight:400;}
  .footer-text{font-size:3.4px;fill:var(--blue);}
  .brand{font-size:4px;font-weight:600;fill:var(--green);}
  .body-line{font-size:3.3px;font-weight:300;}
</style>
</head>
<body>

<svg class="defs" aria-hidden="true">
  <defs>
    <g id="para">
      <text class="body-line" x="0" y="0">Lorem ipsum dolor sit amet, consectetuer</text>
      <text class="body-line" x="0" y="4.4">adipiscing elit, sed diam nonummy nibh</text>
      <text class="body-line" x="0" y="8.8">euismod tincidunt ut laoreet dolore magna</text>
      <text class="body-line" x="0" y="13.2">aliquam erat volutpat. Ut wisi enim ad</text>
      <text class="body-line" x="0" y="17.6">minim veniam, quis nostrud exerci tation</text>
      <text class="body-line" x="0" y="22">ullamcorper suscipit lobortis nisl ut.</text>
    </g>
    <g id="footer">
      <rect x="0" y="216" width="411" height="15" fill="#e8e9ea"/>
      <text class="footer-text" x="21" y="225">PRESENTATION NAME 2022</text>
      <rect x="364" y="220" width="4" height="4" fill="#6cbf43"/>
      <text class="brand" x="370" y="224.5">Molvera</text>
    </g>
    <g id="tick">
      <circle r="3" fill="#0d57a7"/>
      <path d="M-1.4 0 L-0.3 1.1 L1.5 -1" stroke="#fff" stroke-width=".8" fill="none"/>
    </g>
    <g id="tick-white">
      <circle r="3" fill="#fff"/>
      <path d="M-1.4 0 L-0.3 1.1 L1.5 -1" stroke="#0d57a7" stroke-width=".8" fill="none"/>
    </g>
  </defs>
</svg>

<!-- Cover -->
<svg class="slide cover" style="left:507.4px;top:43px" viewBox="0 0 411 231">
  <rect width="411" height="231" fill="#fff"/>
  <rect x="356" y="14" width="6" height="6" fill="var(--green)"/>
  <text x="365" y="20" style="font-size:7px;font-weight:600" fill="var(--green)">Molvera</text>
  <defs><linearGradient id="g-hands" x1="0" x2="1"><stop offset="0" stop-color="#b48a6e"/><stop offset=".55" stop-color="#e9d7c6"/><stop offset="1" stop-color="#f8f3ee"/></linearGradient></defs>
  <rect x="20" y="50" width="391" height="134" fill="url(#g-hands)" role="img" aria-label="Photo of hands forming a heart shape"/>
  <text x="20" y="209" style="font-size:8px;font-weight:400" fill="var(--green)">TAAKDELEGATIE</text>
  <text x="20" y="219" style="font-size:8px;font-weight:400" fill="var(--green)">EN DE CONTROLE</text>
  <rect x="112" y="200" width="299" height="27" fill="var(--blue)"/>
  <text x="128" y="211" class="label" fill="#fff">Lorem ipsum dolor sit amet, consectetuer</text>
  <text x="128" y="217" class="label" fill="#fff">adipiscing elit, sed diam nonummy nibh</text>
</svg>

<!-- Agenda -->
<svg class="slide" style="left:65.7px;top:203.8px" viewBox="0 0 411 231">
  <rect width="411" height="216" fill="var(--blue)"/>
  <text class="title" x="21" y="19" fill="#fff">AGENDA</text>
  <defs><linearGradient id="g-lab" x1="0" x2="1"><stop offset="0" stop-color="#3b4450"/><stop offset=".5" stop-color="#8d96a0"/><stop offset="1" stop-color="#d6d9dc"/></linearGradient></defs>
  <rect x="21" y="47" width="224" height="153" fill="url(#g-lab)" role="img" aria-label="Photo of a clinician reviewing scans at computer screens"/>
  <g class="caps" fill="#fff">
    <text x="258" y="56">02  VISION</text><text x="258" y="66">03  ABOUT</text><text x="258" y="76">04  OUR TEAM</text>
    <text x="258" y="86">05  SUMMARY</text><text x="258" y="96">06  VISION</text><text x="258" y="106">07  ABOUT</text>
    <text x="258" y="116">08  OUR TEAM</text><text x="258" y="126">09  SUMMARY</text><text x="258" y="136">10  VISION</text>
    <text x="258" y="146">11  ABOUT</text><text x="258" y="156">12  OUR TEAM</text><text x="258" y="166">13  SUMMARY</text>
  </g>
  <use href="#para" transform="translate(258 180) scale(.95)" fill="#fff"/>
  <use href="#footer"/>
</svg>

<!-- Our team -->
<svg class="slide" style="left:359.2px;top:203.8px" viewBox="0 0 411 231">
  <polygon points="0,0 372,0 265,216 0,216" fill="var(--blue)"/>
  <polygon points="411,95 411,216 358,216" fill="var(--grey)"/>
  <text class="title" x="21" y="19" fill="#fff">OUR TEAM</text>
  <g fill="#fff">
    <circle cx="31" cy="40" r="8" fill="#c7ccd2"/><circle cx="165" cy="40" r="8" fill="#c7ccd2"/>
    <circle cx="31" cy="142" r="8" fill="#c7ccd2"/><circle cx="165" cy="142" r="8" fill="#c7ccd2"/>
    <text class="small" x="48" y="40">SAM VERHOEVEN</text><text class="small" x="48" y="45">DIRECTOR</text>
    <text class="small" x="182" y="40">SAM VERHOEVEN</text><text class="small" x="182" y="45">DIRECTOR</text>
    <text class="small" x="48" y="142">SAM VERHOEVEN</text><text class="small" x="48" y="147">DIRECTOR</text>
    <text class="small" x="182" y="142">SAM VERHOEVEN</text><text class="small" x="182" y="147">DIRECTOR</text>
  </g>
  <use href="#para" transform="translate(21 60) scale(.85)" fill="#fff"/>
  <use href="#para" transform="translate(155 60) scale(.85)" fill="#fff"/>
  <use href="#para" transform="translate(21 162) scale(.85)" fill="#fff"/>
  <use href="#para" transform="translate(155 162) scale(.85)" fill="#fff"/>
  <use href="#footer"/>
</svg>

<!-- Pricing -->
<svg class="slide" style="left:641.8px;top:203.8px" viewBox="0 0 411 231">
  <polygon points="0,0 411,0 411,35 0,136" fill="var(--grey)"/>
  <text class="title" x="21" y="19" fill="var(--blue)">PRICING</text>
  <use href="#para" transform="translate(21 37) scale(.9)" fill="#7b848c"/>
  <g fill="var(--ink)">
    <line x1="110" y1="118" x2="110" y2="212" stroke="#bbb" stroke-width=".5"/>
    <line x1="205" y1="95" x2="205" y2="190" stroke="#bbb" stroke-width=".5"/>
    <line x1="298" y1="72" x2="298" y2="170" stroke="#bbb" stroke-width=".5"/>
    <text class="label" x="22" y="154">ENTRY LEVEL</text><text x="22" y="174" style="font-size:6px">$3690</text>
    <text class="small" x="30" y="185">• Small meetings</text><text class="small" x="30" y="191">• Small meetings</text><text class="small" x="30" y="197">• Small meetings</text><text class="small" x="30" y="203">• Small meetings</text>
    <text class="label" x="116" y="130">MID-LEVEL</text><text x="116" y="150" style="font-size:6px">$4290</text>
    <text class="small" x="124" y="162">• Small meetings</text><text class="small" x="124" y="168">• Small meetings</text><text class="small" x="124" y="174">• Small meetings</text><text class="small" x="124" y="180">• Small meetings</text>
    <text class="label" x="212" y="110">ADVANCED</text><text x="212" y="129" style="font-size:6px">$4890</text>
    <text class="small" x="220" y="141">• Small meetings</text><text class="small" x="220" y="147">• Small meetings</text><text class="small" x="220" y="153">• Small meetings</text><text class="small" x="220" y="159">• Small meetings</text>
    <text class="label" x="305" y="84">PREMIUM</text><text x="305" y="103" style="font-size:6px">$5490</text>
    <text class="small" x="313" y="114">• Small meetings</text><text class="small" x="313" y="120">• Small meetings</text><text class="small" x="313" y="126">• Small meetings</text><text class="small" x="313" y="132">• Small meetings</text>
  </g>
  <use href="#footer"/>
</svg>

<!-- Graphic 01 -->
<svg class="slide" style="left:914.3px;top:203.8px" viewBox="0 0 411 231">
  <rect width="117" height="216" fill="var(--blue)"/>
  <text class="title" x="21" y="19" fill="#fff">GRAPHIC 01</text>
  <g fill="#fff" class="small"><text x="21" y="40">LOREM IPSUM DOLOR SIT</text><text x="21" y="45">AMET, CONSECTETUER</text><text x="21" y="50">ADIPISCING ELIT, SED DIAM</text><text x="21" y="55">NONUMMY NIBH EUISMOD</text><text x="21" y="60">TINCIDUNT UT LAOREET</text></g>
  <use href="#para" transform="translate(21 86) scale(.85)" fill="#fff"/>
  <use href="#para" transform="translate(21 112) scale(.85)" fill="#fff"/>
  <use href="#para" transform="translate(21 182) scale(.85)" fill="#fff"/>
  <text x="207" y="72" style="font-size:4.5px" fill="var(--ink)">Revenue GeoContribution</text>
  <g class="small" fill="#777" text-anchor="end">
    <text x="150" y="82">40.00%</text><text x="150" y="97">35.00%</text><text x="150" y="113">30.00%</text><text x="150" y="128">25.00%</text>
    <text x="150" y="143">20.00%</text><text x="150" y="159">15.00%</text><text x="150" y="174">10.00%</text><text x="150" y="190">5.00%</text><text x="150" y="205">0.00%</text>
  </g>
  <line x1="155" y1="205" x2="360" y2="205" stroke="#bbb" stroke-width=".4"/>
  <g fill="var(--green)">
    <rect x="165" y="98" width="12" height="107"/><rect x="213" y="106" width="12" height="99"/>
    <rect x="260" y="148" width="12" height="57"/><rect x="308" y="162" width="12" height="43"/>
  </g>
  <g class="small" fill="#555" text-anchor="middle">
    <text x="171" y="95">34.79%</text><text x="219" y="103">32.43%</text><text x="266" y="145">18.64%</text><text x="314" y="159">13.99%</text>
    <text x="171" y="211">Emerging Market</text><text x="219" y="211">US</text><text x="266" y="211">Europe</text><text x="314" y="211">Established</text>
  </g>
  <use href="#footer"/>
</svg>

<!-- Graphic 02 -->
<svg class="slide" style="left:65.7px;top:366.3px" viewBox="0 0 411 231">
  <defs><linearGradient id="g-scan" x1="0" x2="1" y1="0" y2="1"><stop offset="0" stop-color="#6e7fd6"/><stop offset=".5" stop-color="#a7b6ef"/><stop offset="1" stop-color="#3e4c9e"/></linearGradient></defs>
  <rect width="411" height="138" fill="url(#g-scan)" role="img" aria-label="Photo of a patient in a medical scanner"/>
  <text class="title" x="21" y="19" fill="var(--green)">GRAPHIC 02</text>
  <g>
    <circle cx="59" cy="137" r="12" fill="var(--green)"/><circle cx="130" cy="137" r="12" fill="var(--green)"/>
    <circle cx="202" cy="137" r="12" fill="var(--blue)"/><circle cx="273" cy="137" r="12" fill="var(--green)"/>
    <circle cx="345" cy="137" r="12" fill="var(--green)"/>
  </g>
  <g class="small" fill="#fff" text-anchor="middle">
    <text x="59" y="138">2014</text><text x="130" y="138">2015</text><text x="202" y="138">2016</text><text x="273" y="138">2017</text><text x="345" y="138">2018</text>
  </g>
  <g class="small" fill="#555" text-anchor="middle">
    <text x="59" y="162">Project One</text><text x="130" y="162">Project Two</text><text x="202" y="162">Project Tree</text><text x="273" y="162">Project Four</text><text x="345" y="162">Project Five</text>
    <text x="59" y="184">Marketers</text><text x="130" y="184">Marketers</text><text x="202" y="184">Marketers</text><text x="273" y="184">Marketers</text><text x="345" y="184">Marketers</text>
    <text x="59" y="196">To be successful, marketers</text><text x="130" y="196">To be successful, marketers</text><text x="202" y="196">To be successful, marketers</text><text x="273" y="196">To be successful, marketers</text><text x="345" y="196">To be successful, marketers</text>
    <text x="59" y="201">should know the product</text><text x="130" y="201">should know the product</text><text x="202" y="201">should know the product</text><text x="273" y="201">should know the product</text><text x="345" y="201">should know the product</text>
  </g>
  <use href="#footer"/>
</svg>

<!-- Checkmark -->
<svg class="slide" style="left:359.2px;top:366.3px" viewBox="0 0 411 231">
  <text class="title" x="21" y="19" fill="var(--blue)">CHECKMARK</text>
  <use href="#para" transform="translate(21 33) scale(1.05)" fill="var(--ink)"/>
  <use href="#para" transform="translate(21 82) scale(1.05)" fill="var(--ink)"/>
  <polygon points="0,110 411,110 411,140 305,205 0,205" fill="var(--grey-light)"/>
  <g fill="#777" class="small">
    <use href="#tick" x="24" y="122"/><use href="#tick" x="85" y="122"/><use href="#tick" x="146" y="122"/>
    <use href="#tick" x="207" y="122"/><use href="#tick" x="264" y="122"/><use href="#tick" x="326" y="122"/>
    <text x="21" y="132">To protect</text><text x="21" y="137">customers' digital</text><text x="21" y="142">experiences &amp;</text><text x="21" y="147">secure privacy.</text>
    <text x="82" y="132">To protect</text><text x="82" y="137">customers' digital</text><text x="82" y="142">experiences &amp;</text><text x="82" y="147">secure privacy.</text>
    <text x="143" y="132">To protect</text><text x="143" y="137">customers' digital</text><text x="143" y="142">experiences &amp;</text><text x="143" y="147">secure privacy.</text>
    <text x="204" y="132">To protect</text><text x="204" y="137">customers' digital</text><text x="204" y="142">experiences &amp;</text><text x="204" y="147">secure privacy.</text>
    <text x="261" y="132">To protect</text><text x="261" y="137">customers' digital</text><text x="261" y="142">experiences &amp;</text><text x="261" y="147">secure privacy.</text>
    <text x="323" y="132">To protect</text><text x="323" y="137">customers' digital</text><text x="323" y="142">experiences &amp;</text><text x="323" y="147">secure privacy.</text>
  </g>
  <use href="#footer"/>
</svg>

<!-- Graphic 03 -->
<svg class="slide" style="left:641.8px;top:366.3px" viewBox="0 0 411 231">
  <rect x="318" width="93" height="216" fill="var(--grey-light)"/>
  <text class="title" x="21" y="19" fill="var(--ink)">GRAPHIC 03</text>
  <g class="small" fill="#555" text-anchor="middle"><text x="63" y="50">Sales</text><text x="221" y="50">Sales</text></g>
  <g transform="translate(63 98)">
    <circle r="41" fill="#e3e4e5"/>
    <path d="M0 0 L0 -41 A41 41 0 1 1 -23 34 Z" fill="var(--blue)"/>
    <path d="M0 0 L-23 34 A41 41 0 0 1 -40 -8 Z" fill="var(--green)"/>
    <path d="M0 0 L-40 -8 A41 41 0 0 1 -24 -33 Z" fill="#c6c8ca"/>
    <path d="M0 -41 L0 0 L-24 -33 A41 41 0 0 1 0 -41 Z" fill="#f0f0f0"/>
  </g>
  <g transform="translate(221 98)">
    <circle r="41" fill="#e3e4e5"/>
    <path d="M0 0 L0 -41 A41 41 0 1 1 -23 34 Z" fill="var(--blue)"/>
    <path d="M0 0 L-23 34 A41 41 0 0 1 -40 -8 Z" fill="var(--green)"/>
    <path d="M0 0 L-40 -8 A41 41 0 0 1 -24 -33 Z" fill="#c6c8ca"/>
  </g>
  <g class="small" fill="#777"><text x="25" y="149">• 1st Qtr  • 2nd Qtr  • 3rd Qtr  • 4th Qtr</text><text x="183" y="149">• 1st Qtr  • 2nd Qtr  • 3rd Qtr  • 4th Qtr</text></g>
  <use href="#para" transform="translate(21 162) scale(1.05)" fill="var(--ink)"/>
  <use href="#para" transform="translate(178 162) scale(1.05)" fill="var(--ink)"/>
  <use href="#footer"/>
</svg>

<!-- About us -->
<svg class="slide" style="left:914.3px;top:366.3px" viewBox="0 0 411 231">
  <text class="title" x="21" y="22" fill="var(--blue)">ABOUT US</text>
  <rect y="44" width="411" height="56" fill="var(--blue)"/>
  <g class="label" fill="#fff"><text x="21" y="59">LOREM IPSUM DOLOR SIT AMET, CONSECTETUER ADIPISCING</text><text x="21" y="66">ELIT, SED DIAM NONUMMY NIBH EUISMOD TINCIDUNT UT</text><text x="21" y="73">LAOREET DOLORE MAGNA ALIQUAM ERAT VOLUTPAT. UT WISI</text><text x="21" y="80">ENIM AD MINIM VENIAM, QUIS NOSTRUD EXERCI TATION</text><text x="21" y="87">ULLAMCORPER SUSCIPIT LOBORTIS NISL UT ALIQUIP EX EA</text></g>
  <use href="#para" transform="translate(21 122) scale(1.05)" fill="var(--ink)"/>
  <use href="#para" transform="translate(21 152) scale(1.05)" fill="var(--ink)"/>
  <use href="#para" transform="translate(162 122) scale(1.05)" fill="var(--ink)"/>
  <use href="#para" transform="translate(162 152) scale(1.05)" fill="var(--ink)"/>
  <use href="#footer"/>
</svg>

<!-- About us 2 -->
<svg class="slide" style="left:65.7px;top:547.4px" viewBox="0 0 411 231">
  <defs><linearGradient id="g-micro" x1="0" x2="1"><stop offset="0" stop-color="#c9ccd1"/><stop offset=".5" stop-color="#eef0f2"/><stop offset="1" stop-color="#6b7480"/></linearGradient></defs>
  <polygon points="240,0 411,0 411,216 195,216" fill="url(#g-micro)" role="img" aria-label="Photo of a researcher working at a microscope in a lab"/>
  <text class="title" x="21" y="19" fill="var(--ink)">ABOUT US 2</text>
  <g class="label" fill="var(--blue)"><text x="21" y="69">LOREM IPSUM DOLOR SIT</text><text x="21" y="75">AMET, CONSECTETUER</text><text x="21" y="81">ADIPISCING ELIT, SED DIAM</text><text x="21" y="87">NONUMMY NIBH EUISMOD</text><text x="21" y="93">TINCIDUNT UT LAOREET</text></g>
  <use href="#para" transform="translate(126 66) scale(.85)" fill="var(--ink)"/>
  <use href="#para" transform="translate(126 92) scale(.85)" fill="var(--ink)"/>
  <use href="#para" transform="translate(126 118) scale(.85)" fill="var(--ink)"/>
  <use href="#para" transform="translate(126 144) scale(.85)" fill="var(--ink)"/>
  <use href="#footer"/>
</svg>

<!-- Table -->
<svg class="slide" style="left:359.2px;top:547.4px" viewBox="0 0 411 231">
  <text class="title" x="21" y="19" fill="var(--blue)">TABLE</text>
  <rect y="32" width="411" height="70" fill="var(--green)"/>
  <use href="#para" transform="translate(21 40) scale(1.05)" fill="#fff"/>
  <use href="#para" transform="translate(180 40) scale(1.05)" fill="#fff"/>
  <use href="#para" transform="translate(21 86) scale(1.05)" fill="#fff"/>
  <rect x="21" y="109" width="111" height="6" fill="var(--blue)"/><rect x="137" y="109" width="93" height="6" fill="var(--blue)"/>
  <g class="small" fill="#fff"><text x="28" y="113.5">BASE</text><text x="140" y="113.5">SCORE</text></g>
  <g fill="var(--grey-light)">
    <rect x="21" y="120" width="111" height="6"/><rect x="137" y="120" width="93" height="6"/>
    <rect x="21" y="131" width="111" height="6"/><rect x="137" y="131" width="93" height="6"/>
    <rect x="21" y="142" width="111" height="6"/><rect x="137" y="142" width="93" height="6"/>
    <rect x="21" y="153" width="111" height="6"/><rect x="137" y="153" width="93" height="6"/>
    <rect x="21" y="164" width="111" height="6"/><rect x="137" y="164" width="93" height="6"/>
    <rect x="21" y="175" width="111" height="6"/><rect x="137" y="175" width="93" height="6"/>
    <rect x="21" y="186" width="111" height="6"/><rect x="137" y="186" width="93" height="6"/>
    <rect x="21" y="197" width="111" height="6"/><rect x="137" y="197" width="93" height="6"/>
  </g>
  <g class="small" fill="#555">
    <text x="28" y="124.5">AVERAGE MONTHLY QUOTES</text><text x="140" y="124.5">432</text>
    <text x="28" y="135.5">AVERAGE MONTHLY QUOTES</text><text x="140" y="135.5">946</text>
    <text x="28" y="146.5">AVERAGE MONTHLY QUOTES</text><text x="140" y="146.5">330</text>
    <text x="28" y="157.5">AVERAGE MONTHLY QUOTES</text><text x="140" y="157.5">432</text>
    <text x="28" y="168.5">AVERAGE MONTHLY QUOTES</text><text x="140" y="168.5">946</text>
    <text x="28" y="179.5">AVERAGE MONTHLY QUOTES</text><text x="140" y="179.5">330</text>
    <text x="28" y="190.5">AVERAGE MONTHLY QUOTES</text><text x="140" y="190.5">946</text>
    <text x="28" y="201.5">AVERAGE MONTHLY QUOTES</text><text x="140" y="201.5">330</text>
  </g>
  <use href="#footer"/>
</svg>

<!-- Benefits -->
<svg class="slide" style="left:641.8px;top:547.4px" viewBox="0 0 411 231">
  <defs><radialGradient id="g-eye" cx=".5" cy=".4" r=".7"><stop offset="0" stop-color="#6fa7b6"/><stop offset=".6" stop-color="#2c4a58"/><stop offset="1" stop-color="#17222a"/></radialGradient></defs>
  <rect width="172" height="216" fill="url(#g-eye)" role="img" aria-label="Close-up photo of an eye with digital overlay"/>
  <text class="title" x="21" y="19" fill="#fff">BENEFITS</text>
  <circle cx="76" cy="157" r="40" fill="var(--green)"/>
  <circle cx="143" cy="155" r="30" fill="var(--blue)"/>
  <g class="label" fill="#fff" text-anchor="middle"><text x="76" y="154">TOTAL</text><text x="76" y="161">BENEFITS</text><text x="143" y="157">1296</text></g>
  <g class="small" fill="var(--ink)">
    <text x="186" y="31">VENIAM, QUIS NOSTRUD EXERCI TATION ULLAMCORPER SUSCIPIT</text>
    <text x="186" y="36">LOBORTIS NISL UT ALIQUIP EX EA COMMODO CONSEQUAT. DUIS</text>
    <text x="186" y="41">AUTEM VEL EUM IRIURE DOLOR IN HENDRERIT IN VULPUTATE</text>
    <text x="186" y="46">VELIT ESSE MOLESTIE CONSEQUAT, VEL ILLUM DOLORE EU</text>
    <text x="186" y="51">FEUGIAT NULLA FACILISIS AT VERO EROS ET ACCUMSAN</text>
    <text x="186" y="56">ALIQUIP EX EA COMMODO</text>
    <text x="186" y="99" class="label">BENEFITS</text>
    <text x="196" y="112">•  Lorem ipsum dolor sit amet, consectetuer adipiscing elit, sed diam</text>
    <text x="199" y="117">nonummy nibh euismod</text>
    <text x="196" y="130">•  Incidunt ut laoreet dolore magna aliquam</text>
    <text x="196" y="144">•  Erat volutpat. Ut wisi enim ad minim veniam, quis nostrud exerci</text>
    <text x="199" y="149">tation ullamcorper suscipit lobortis nisl ut aliquip ex ea</text>
    <text x="196" y="163">•  Lobortis nisl ut aliquip ex ea commodo veniam</text>
  </g>
  <use href="#footer"/>
</svg>

<!-- Break -->
<svg class="slide" style="left:914.3px;top:543.2px" viewBox="0 0 411 231">
  <defs><linearGradient id="g-pills" x1="0" x2="1" y1="0" y2="1"><stop offset="0" stop-color="#57a3e4"/><stop offset=".6" stop-color="#6aaeea"/><stop offset="1" stop-color="#4d95d6"/></linearGradient></defs>
  <rect width="411" height="216" fill="url(#g-pills)" role="img" aria-label="Photo of pills spilling from an orange bottle on a blue surface"/>
  <polygon points="190,0 411,0 411,122" fill="#fff"/>
  <text class="title" x="21" y="19" fill="#fff">BREAK</text>
  <use href="#footer"/>
</svg>

<!-- Graphic -->
<svg class="slide" style="left:65.7px;top:720.1px" viewBox="0 0 411 231">
  <rect width="411" height="216" fill="var(--blue)"/>
  <text class="title" x="21" y="19" fill="#fff">GRAPHIC</text>
  <g fill="none" stroke="#fff" stroke-width=".9">
    <path d="M205 29 l7 2.5 v5 c0 4 -3 6.5 -7 8 c-4 -1.5 -7 -4 -7 -8 v-5 z"/><path d="M202 37 l2 2 l4 -4"/>
    <circle cx="125" cy="85" r="2"/><path d="M120 89 h10 M125 89 v8 l-2.5 5 M125 97 l2.5 5"/>
    <path d="M284 86 l6 14 l2 -5 l5 -2 z M288 80 v-3 M282 82 l-2 -2 M294 82 l2 -2"/>
    <rect x="200" y="155" width="10" height="9"/><path d="M200 158 h10 M203 153 v3 M207 153 v3"/><circle cx="212" cy="163" r="3"/>
  </g>
  <g class="small" fill="#fff" text-anchor="middle">
    <text x="205" y="57">Lorem ipsum dolor sit amet, consectetuer</text><text x="205" y="62">adipiscing elit, sed diam nonummy nibh</text><text x="205" y="67">euismod tincidunt ut laoreet dolore magna</text>
    <text x="125" y="114">Lorem ipsum dolor sit amet, consectetuer</text><text x="125" y="119">adipiscing elit, sed diam nonummy nibh</text><text x="125" y="124">euismod tincidunt ut laoreet dolore magna</text>
    <text x="290" y="114">Lorem ipsum dolor sit amet, consectetuer</text><text x="290" y="119">adipiscing elit, sed diam nonummy nibh</text><text x="290" y="124">euismod tincidunt ut laoreet dolore magna</text>
    <text x="205" y="183">Lorem ipsum dolor sit amet, consectetuer</text><text x="205" y="188">adipiscing elit, sed diam nonummy nibh</text><text x="205" y="193">euismod tincidunt ut laoreet dolore magna</text>
  </g>
  <use href="#footer"/>
</svg>

<!-- Sector expertise -->
<svg class="slide" style="left:359.2px;top:720.1px" viewBox="0 0 411 231">
  <rect x="112" width="98" height="216" fill="var(--grey-light)"/>
  <rect x="315" width="96" height="216" fill="var(--grey-light)"/>
  <text class="title" x="21" y="19" fill="var(--blue)">SECTOR</text>
  <text class="title" x="21" y="31" fill="var(--blue)">EXPERTISE</text>
  <g class="label" fill="var(--blue)"><text x="21" y="51">1.</text><text x="122" y="51">2.</text><text x="224" y="51">3.</text><text x="325" y="51">4.</text></g>
  <use href="#para" transform="translate(21 64) scale(.85)" fill="var(--ink)"/>
  <use href="#para" transform="translate(122 64) scale(.85)" fill="var(--ink)"/>
  <use href="#para" transform="translate(224 64) scale(.85)" fill="var(--ink)"/>
  <use href="#para" transform="translate(325 64) scale(.85)" fill="var(--ink)"/>
  <polygon points="21,118 72,118 92,142 92,216 21,216" fill="#c8cacc"/>
  <polygon points="122,118 173,118 194,142 194,216 122,216" fill="var(--blue)"/>
  <polygon points="224,118 275,118 295,142 295,216 224,216" fill="#c8cacc"/>
  <polygon points="325,118 376,118 396,142 396,216 325,216" fill="var(--blue)"/>
  <g fill="none" stroke="#fff" stroke-width=".8">
    <circle cx="40" cy="127" r="4"/><path d="M135 124 l4 4 l4 -4 M133 132 h10"/><path d="M238 127 a5 5 0 0 1 10 0 z M243 127 v6"/><path d="M334 132 v-7 h8 v7 M336 130 l2 -2 l2 2"/>
  </g>
  <g class="small" fill="#fff"><text x="33" y="143">LOREM IPSUM</text><text x="33" y="148">DOLOR SIT AMET,</text><text x="33" y="153">CONSECTETUER</text>
    <text x="134" y="143">LOREM IPSUM</text><text x="134" y="148">DOLOR SIT AMET,</text><text x="134" y="153">CONSECTETUER</text>
    <text x="236" y="143">LOREM IPSUM</text><text x="236" y="148">DOLOR SIT AMET,</text><text x="236" y="153">CONSECTETUER</text>
    <text x="337" y="143">LOREM IPSUM</text><text x="337" y="148">DOLOR SIT AMET,</text><text x="337" y="153">CONSECTETUER</text></g>
  <use href="#footer"/>
</svg>

<!-- Competences -->
<svg class="slide" style="left:641.8px;top:720.1px" viewBox="0 0 411 231">
  <polygon points="0,0 253,0 0,206" fill="var(--green)"/>
  <text class="title" x="21" y="19" fill="#fff">COMPETENCES</text>
  <g fill="var(--blue)">
    <rect x="185" y="45" width="14" height="14" transform="rotate(45 192 52)"/>
    <rect x="143" y="78" width="14" height="14" transform="rotate(45 150 85)"/>
    <rect x="106" y="110" width="14" height="14" transform="rotate(45 113 117)"/>
    <rect x="63" y="141" width="14" height="14" transform="rotate(45 70 148)"/>
    <rect x="26" y="175" width="14" height="14" transform="rotate(45 33 182)"/>
  </g>
  <g fill="none" stroke="#fff" stroke-width=".7">
    <path d="M188 55 h8 M189 55 v-5 M195 55 v-5 M188 50 l4 -3 l4 3"/>
    <circle cx="113" cy="117" r="0"/><path d="M109 119 l3 -3 l2 2 l4 -4"/>
    <circle cx="70" cy="146" r="2"/><path d="M66 152 a4 4 0 0 1 8 0"/>
    <path d="M29 182 h8 M31 180 l4 4"/>
  </g>
  <text x="150" y="86.5" style="font-size:4px" fill="#fff" text-anchor="middle">$$$</text>
  <g class="small" fill="var(--ink)">
    <text x="210" y="50">LOREM IPSUM DOLOR SIT AMET,</text><text x="210" y="55">CONSECTETUER ADIPISCING ELIT.</text>
    <text x="168" y="83">LOREM IPSUM DOLOR SIT AMET,</text><text x="168" y="88">CONSECTETUER ADIPISCING ELIT.</text>
    <text x="131" y="115">LOREM IPSUM DOLOR SIT AMET,</text><text x="131" y="120">CONSECTETUER ADIPISCING ELIT.</text>
    <text x="88" y="146">LOREM IPSUM DOLOR SIT AMET,</text><text x="88" y="151">CONSECTETUER ADIPISCING ELIT.</text>
    <text x="51" y="180">LOREM IPSUM DOLOR SIT AMET,</text><text x="51" y="185">CONSECTETUER ADIPISCING ELIT.</text>
  </g>
  <use href="#footer"/>
</svg>

<!-- Graphic 04 -->
<svg class="slide" style="left:914.3px;top:720.1px" viewBox="0 0 411 231">
  <polygon points="0,0 165,0 0,196" fill="var(--grey-light)"/>
  <rect x="245" width="150" height="216" fill="var(--green)"/>
  <text class="title" x="252" y="22" fill="#fff">GRAPHIC 04</text>
  <use href="#para" transform="translate(252 82) scale(.95)" fill="#fff"/>
  <use href="#para" transform="translate(252 112) scale(.95)" fill="#fff"/>
  <use href="#para" transform="translate(252 160) scale(.95)" fill="#fff"/>
  <g>
    <circle cx="128" cy="49" r="9" fill="var(--green)"/><circle cx="70" cy="80" r="9" fill="var(--blue)"/>
    <circle cx="185" cy="80" r="9" fill="var(--green)"/><circle cx="70" cy="147" r="9" fill="var(--blue)"/>
    <circle cx="185" cy="147" r="9" fill="var(--blue)"/><circle cx="128" cy="178" r="9" fill="var(--green)"/>
  </g>
  <g fill="none" stroke="#fff" stroke-width=".7">
    <circle cx="128" cy="48" r="3"/><path d="M127 52 h2"/>
    <circle cx="70" cy="78" r="2.5"/><path d="M66 85 h8"/>
    <circle cx="185" cy="78" r="2"/><path d="M181 85 a4 4 0 0 1 8 0"/>
    <circle cx="69" cy="146" r="3"/><path d="M71 148 l3 3"/>
    <rect x="181" y="144" width="8" height="5"/>
    <path d="M128 173 l4 1.5 v3 c0 2.5 -2 4 -4 5 c-2 -1 -4 -2.5 -4 -5 v-3 z"/>
  </g>
  <g class="small" fill="#555" text-anchor="middle">
    <text x="128" y="66">MANAGEMENT</text><text x="70" y="97">MANAGEMENT</text><text x="185" y="97">MANAGEMENT</text>
    <text x="70" y="164">MANAGEMENT</text><text x="185" y="164">MANAGEMENT</text><text x="128" y="195">MANAGEMENT</text>
  </g>
  <use href="#footer"/>
</svg>

<!-- Methods of differentiation -->
<svg class="slide" style="left:65.7px;top:893.4px" viewBox="0 0 411 231">
  <defs><linearGradient id="g-methods" x1="0" x2="1" y1="0" y2="1"><stop offset="0" stop-color="#2f5fae"/><stop offset=".5" stop-color="#3b6cba"/><stop offset="1" stop-color="#26539c"/></linearGradient></defs>
  <rect width="411" height="216" fill="url(#g-methods)" role="img" aria-label="Blue-toned photo of hands at a desk with a stethoscope"/>
  <text class="title" x="21" y="19" fill="#fff">METHODS OF</text>
  <text class="title" x="21" y="31" fill="#fff">DIFFERENTIATION</text>
  <use href="#tick-white" x="74" y="61"/><use href="#tick-white" x="205" y="95"/><use href="#tick-white" x="335" y="61"/>
  <g class="small" fill="#fff" text-anchor="middle">
    <text x="74" y="78">Network of Providers</text><text x="74" y="92">Lorem ipsum dolor sit amet,</text><text x="74" y="97">consectetuer adipiscing elit, sed</text><text x="74" y="102">diam nonummy nibh euismod</text><text x="74" y="107">ipsum dolor sit amet</text>
    <text x="205" y="112">Network of Providers</text><text x="205" y="126">Lorem ipsum dolor sit amet,</text><text x="205" y="131">consectetuer adipiscing elit, sed</text><text x="205" y="136">diam nonummy nibh euismod</text><text x="205" y="141">ipsum dolor sit amet</text>
    <text x="335" y="78">Network of Providers</text><text x="335" y="92">Lorem ipsum dolor sit amet,</text><text x="335" y="97">consectetuer adipiscing elit, sed</text><text x="335" y="102">diam nonummy nibh euismod</text><text x="335" y="107">ipsum dolor sit amet</text>
  </g>
  <use href="#footer"/>
</svg>

<!-- About us (code) -->
<svg class="slide" style="left:359.2px;top:893.4px" viewBox="0 0 411 231">
  <defs><linearGradient id="g-code" x1="0" x2="1" y1="0" y2="1"><stop offset="0" stop-color="#1e2c44"/><stop offset=".5" stop-color="#3c5a86"/><stop offset="1" stop-color="#0e1626"/></linearGradient></defs>
  <rect width="147" height="216" fill="url(#g-code)" role="img" aria-label="Photo of programming code on a screen"/>
  <text class="title" x="21" y="19" fill="#fff">ABOUT US</text>
  <use href="#para" transform="translate(166 30) scale(.95)" fill="var(--ink)"/>
  <use href="#para" transform="translate(166 56) scale(.95)" fill="var(--ink)"/>
  <use href="#para" transform="translate(166 82) scale(.95)" fill="var(--ink)"/>
  <use href="#para" transform="translate(288 30) scale(.95)" fill="var(--ink)"/>
  <use href="#para" transform="translate(288 56) scale(.95)" fill="var(--ink)"/>
  <use href="#para" transform="translate(288 82) scale(.95)" fill="var(--ink)"/>
  <g class="small" fill="var(--ink)"><text x="166" y="148">Lorem ipsum dolor sit amet, cons</text><text x="288" y="148">Lorem ipsum dolor sit amet, cons</text></g>
  <use href="#footer"/>
</svg>

<!-- Outline -->
<svg class="slide" style="left:641.8px;top:893.4px" viewBox="0 0 411 231">
  <text class="title" x="21" y="19" fill="var(--ink)">OUTLINE</text>
  <g fill="#cfd1d3">
    <rect x="16" y="56" width="86" height="39"/><rect x="105" y="56" width="86" height="39"/><rect x="202" y="56" width="86" height="39"/><rect x="290" y="56" width="86" height="39"/>
    <rect x="16" y="111" width="86" height="39"/><rect x="105" y="111" width="86" height="39"/><rect x="202" y="111" width="86" height="39"/><rect x="290" y="111" width="86" height="39"/>
  </g>
  <g fill="#fff">
    <text x="27" y="81" style="font-size:12px;font-weight:300">1.</text><text x="42" y="80" class="label">SUMMARY</text>
    <text x="116" y="81" style="font-size:12px;font-weight:300">2.</text><text x="131" y="80" class="label">VISION</text>
    <text x="213" y="81" style="font-size:12px;font-weight:300">3.</text><text x="228" y="80" class="label">SUMMARY</text>
    <text x="301" y="81" style="font-size:12px;font-weight:300">4.</text><text x="316" y="80" class="label">VISION</text>
    <text x="27" y="136" style="font-size:12px;font-weight:300">5.</text><text x="42" y="135" class="label">SUMMARY</text>
    <text x="116" y="136" style="font-size:12px;font-weight:300">6.</text><text x="131" y="135" class="label">VISION</text>
    <text x="213" y="136" style="font-size:12px;font-weight:300">7.</text><text x="228" y="135" class="label">SUMMARY</text>
    <text x="301" y="136" style="font-size:12px;font-weight:300">8.</text><text x="316" y="135" class="label">VISION</text>
  </g>
  <use href="#para" transform="translate(16 178) scale(1.05)" fill="var(--ink)"/>
  <use href="#para" transform="translate(125 178) scale(1.05)" fill="var(--ink)"/>
  <use href="#footer"/>
</svg>

<!-- Thank you -->
<svg class="slide" style="left:914.3px;top:893.4px" viewBox="0 0 411 231">
  <polygon points="0,0 411,0 411,95 0,200" fill="var(--green)"/>
  <text x="21" y="28" style="font-size:13px;font-weight:300" fill="#fff">THANK YOU</text>
  <line x1="21" y1="46" x2="41" y2="46" stroke="#fff" stroke-width=".6"/>
  <g fill="#fff" style="font-size:6px;font-weight:300"><text x="21" y="63">LOREM IPSUM DOLOR SIT</text><text x="21" y="71">AMET, CONSECTETUER</text><text x="21" y="79">ADIPISCING ELIT, SED DI</text></g>
  <rect x="364" y="220" width="4" height="4" fill="var(--green)"/>
  <text class="brand" x="370" y="224.5">Molvera</text>
</svg>

</body>
</html>
```